Simple : A Therapist is looking for a Design

Im lookind for a business card design for my new business .
my therapy field - Stillpoint Cranial .
Its part of Osteopatic medicine .
its gental, not invasive method that focus on the bones of the skull (cranial) .
i want some kind of skull in it like the attached photo.

Target Market(s)

people that suffer from pain

Industry/Entity Type

Physical Therapy

Contact Information for Business Card

i want people to understand this is diffrent kind of therapy
its anatomy base , gental and give outstanding result .

Font styles to use
Serif

Colors
fee18a
cadf82
fbc994
cedeed
fbe7d2
fff3d1

Requirements
Must have
• one side: my name (Yoram Shefet) ,
• phone number ( 0521746098)
• email (shefetyoram@postvela.com)
• other side : Stillpoint Cranial
Nice to have
• i want some kind of skull in it like the attached photo.
• very powrful, accurate and smart.
• nice colores (maybe lite orange?, lite green?) , simple, relax, smart

```html
<!DOCTYPE html>
<html lang="en">
<head>
<meta charset="utf-8">
<title>Stillpoint Cranial – Business Card</title>
<link rel="stylesheet" href="https://fonts.googleapis.com/css2?family=Lato:wght@400;700;900&family=Poppins:wght@300&display=swap">
<style>
  :root {
    --page-bg: #1c1c1c;
    --card-bg: #0d0d0e;
    --card-edge: #1a1a1b;
    --logo-grey: #a3a3a3;
    --logo-dot: #cadf82;
    --name-yellow: #fee18a;
    --name-green: #cadf82;
    --text-light: #d9d9d9;
    --icon-yellow: #fee18a;
  }
  * { margin: 0; padding: 0; box-sizing: border-box; }
  html, body {
    width: 1200px;
    height: 900px;
    overflow: hidden;
    background: var(--page-bg);
  }
  .canvas {
    position: relative;
    width: 1200px;
    height: 900px;
  }
  .card {
    position: absolute;
    width: 600px;
    height: 343px;
    border-radius: 26px;
    background: var(--card-bg);
    border: 1px solid var(--card-edge);
    box-shadow: 0 18px 40px rgba(0, 0, 0, 0.55);
  }
  .card--back { left: 140px; top: 80px; }
  .card--front { left: 460px; top: 476px; }

  .brand {
    position: absolute;
    display: flex;
    align-items: center;
    gap: 14px;
    font-family: "Poppins", sans-serif;
    font-weight: 300;
    color: var(--logo-grey);
    white-space: nowrap;
  }
  .brand__dot {
    width: 16px;
    height: 16px;
    border-radius: 50%;
    background: var(--logo-grey);
    flex: none;
  }
  .card--back .brand {
    left: 50%;
    top: 50%;
    transform: translate(-50%, -50%);
    font-size: 40px;
  }
  .card--front .brand {
    right: 36px;
    top: 58px;
    font-size: 34px;
  }
  .card--front .brand__dot { background: var(--logo-dot); }

  .contact {
    position: absolute;
    left: 40px;
    bottom: 40px;
    font-family: "Lato", sans-serif;
  }
  .contact__name {
    font-weight: 900;
    font-size: 22px;
    letter-spacing: 1.5px;
    text-transform: uppercase;
    margin-bottom: 26px;
  }
  .contact__first { color: var(--name-yellow); }
  .contact__last { color: var(--name-green); }
  .contact__line {
    display: flex;
    align-items: center;
    gap: 8px;
    font-size: 19px;
    color: var(--text-light);
    line-height: 1.45;
  }
  .contact__icon { width: 16px; height: 16px; flex: none; }
</style>
</head>
<body>
<main class="canvas">

  <section class="card card--back" aria-label="Card back">
    <div class="brand">
      <span class="brand__dot"></span>
      <span class="brand__name">Stillpoint Cranial</span>
    </div>
  </section>

  <section class="card card--front" aria-label="Card front">
    <div class="brand">
      <span class="brand__dot"></span>
      <span class="brand__name">Stillpoint Cranial</span>
    </div>

    <div class="contact">
      <p class="contact__name">
        <span class="contact__first">Yoram</span>
        <span class="contact__last">Shefet</span>
      </p>
      <p class="contact__line">
        <svg class="contact__icon" viewBox="0 0 16 16" aria-hidden="true">
          <path fill="var(--icon-yellow)" d="M3 6c0-2 1-3 5-3s5 1 5 3l-2 1-1-2H6L5 7 3 6zm1 2h8l1 5H3l1-5zm4 1.2a1.6 1.6 0 1 0 0 3.2 1.6 1.6 0 0 0 0-3.2z"/>
        </svg>
        <span>0521746098</span>
      </p>
      <p class="contact__line">
        <svg class="contact__icon" viewBox="0 0 16 16" aria-hidden="true">
          <rect x="1" y="3" width="14" height="10" rx="1" fill="var(--icon-yellow)"/>
          <path d="M1.5 3.5 8 9l6.5-5.5" fill="none" stroke="var(--card-bg)" stroke-width="1.3"/>
        </svg>
        <span>shefetyoram@postvela.com</span>
      </p>
    </div>
  </section>

</main>
</body>
</html>
```